A professional business to business web site for a contract agency called VONTAREX.

We need a very clean, very professional web site created for business to business. It is an informational web site with 3 pages. We are a company that offers contract employee placements into primarily the pharmaceutical industry. I have attached a file that describes the company more fully.

Hi,

I'm sorry if I wasn't clear, but I need to have the HTML pages created so I can just upload the files you give me to the web hosting site.

Please let me know if you have any questions.

Thanks for working on my project!

Hello,

I didn't put this in the description, but I would need the web site set up on the web hosting site as well.  The web hosting site is abrightkettle.  I want a copy of all the files as well.

Thanks,
Miles

Reason: I'm sorry, unexpectedly, I have been very busy and I haven't been able to devote the time necessary for this. I am extending the deadline by 10 days. Thank you for your patience. Thanks.

Reason: Hi everyone, I apologize again, but everything has been so busy here that I haven't been able to give this attention. I plan to work on this over the next few days. Thanks and sorry again, Miles.

Reason: I'm sorry this is taking longer than planned. I have been extremely busy. I have increased the budget on this project. Thanks.

Target Market(s)

Large professional corporations mainly in the pharmaceutical industry. The audience is hiring decisions makers within the companies and potential job candidates/job seekers.

Industry/Entity Type

Pharmaceutical

Font styles to use
Sans Serif

Requirements
Must have
• Must have a clean look that mimics the pharmaceutical industry web sites. VERY professional.
Nice to have
• A nice picture of professional business/pharma/technical people looking like a team. Colors are listed on the attached Word document.
Should not have
• No animation. Not too busy.

```html
<!DOCTYPE html>
<html lang="en">
<head>
<meta charset="utf-8">
<title>VONTAREX</title>
<link rel="stylesheet" href="https://fonts.googleapis.com/css2?family=Open+Sans:wght@400;600;700&family=Arimo:wght@400&display=swap">
<style>
  :root {
    --brand-blue: #0f4c8a;
    --title-blue: #16498f;
    --navy: #0c3566;
    --footer-blue: #0e3b6f;
    --teal: #1fb89a;
    --text-grey: #8a8a8a;
    --text-dark: #444;
    --line: #e2e2e2;
    --panel: #f4f4f4;
    --white: #ffffff;
  }
  * { margin: 0; padding: 0; box-sizing: border-box; }
  html, body { width: 1200px; height: 2230px; overflow: hidden; }
  body { position: relative; background: var(--white); font-family: "Open Sans", Arial, sans-serif; color: var(--text-dark); }
  .abs { position: absolute; }

  /* Hero */
  .hero { left: 0; top: 0; width: 1200px; height: 680px; overflow: hidden;
    background: radial-gradient(ellipse at 30% 40%, #d9e4e6 0%, #e8e2e0 35%, #ece9e7 70%, #dfe3e4 100%); }
  .hero-visual { position: absolute; inset: 0;
    background: radial-gradient(ellipse 260px 120px at 640px 360px, rgba(214,140,150,.45), transparent 70%),
                radial-gradient(ellipse 200px 160px at 110px 80px, rgba(110,190,190,.35), transparent 70%); }
  .hero-title { top: 285px; width: 100%; text-align: center; color: var(--title-blue); font-size: 58px; font-weight: 400; letter-spacing: 1px; }
  .hero-sub { top: 366px; width: 100%; text-align: center; color: var(--white); font-size: 44px; font-weight: 400; line-height: 60px; }
  .btn { display: block; text-align: center; color: var(--white); font-size: 24px; line-height: 56px; height: 56px; }
  .btn-register { left: 428px; top: 514px; width: 164px; background: var(--title-blue); }
  .btn-login { left: 608px; top: 514px; width: 164px; background: var(--teal); }
  .slider-nav { left: 548px; top: 622px; width: 104px; height: 104px; border-radius: 50%; background: var(--white); border: 3px solid #e6e6e6; }

  /* Header */
  .site-header { left: 131px; top: 0; width: 937px; height: 110px; background: var(--white); border-top: 4px solid var(--navy); box-shadow: 0 2px 6px rgba(0,0,0,.25); }
  .brand { position: absolute; left: 18px; top: 34px; display: flex; align-items: center; gap: 10px; }
  .brand-dot { width: 26px; height: 26px; border-radius: 50%; background: var(--title-blue); }
  .brand-name { font-size: 30px; font-weight: 600; color: var(--title-blue); letter-spacing: 4px; }
  .social { position: absolute; right: 24px; top: 26px; display: flex; gap: 16px; }
  .social span { width: 12px; height: 12px; border-radius: 50%; background: #b9b9b9; }
  .main-nav { position: absolute; right: 24px; top: 64px; display: flex; gap: 31px; font-size: 14px; color: #555; }
  .main-nav .active { color: var(--title-blue); font-weight: 600; }

  /* Team band */
  .team { left: 0; top: 680px; width: 1200px; height: 435px; background: var(--brand-blue); color: var(--white); }
  .team-title { position: absolute; top: 32px; width: 100%; text-align: center; font-size: 29px; font-weight: 600; }
  .team-card { position: absolute; top: 98px; width: 300px; text-align: center; }
  .team-photo { width: 204px; height: 204px; margin: 0 auto; border-radius: 50%; border: 4px solid #0a3766; box-shadow: 0 0 0 2px #2f6aa6; }
  .photo-lab { background: radial-gradient(circle at 45% 40%, #f2f2f2, #9aa7b4 70%, #5d6f82); }
  .photo-glass { background: radial-gradient(circle at 50% 45%, #c47a4f, #6b4a38 60%, #2a2320); }
  .photo-vial { background: radial-gradient(circle at 55% 50%, #b5303a, #e8d8d8 50%, #cfd9dd); }
  .team-card h3 { margin-top: 28px; color: var(--teal); font-size: 20px; font-weight: 600; }
  .team-card p { margin-top: 6px; font-size: 12.5px; line-height: 18px; font-weight: 600; }

  /* Welcome */
  .welcome-title { top: 1153px; width: 100%; text-align: center; color: var(--title-blue); font-size: 27px; font-weight: 700; }
  .welcome-text { left: 130px; top: 1204px; width: 940px; text-align: center; font-family: "Arimo", Arial, sans-serif; font-size: 14.5px; line-height: 26.5px; color: var(--text-grey); }
  .btn-more { left: 510px; top: 1340px; width: 181px; height: 42px; border: 1px solid #ddd; border-radius: 3px; background: #fafafa; font-size: 14px; color: #333; text-align: center; line-height: 40px; }

  /* People strip */
  .people { left: 0; top: 1422px; width: 1200px; height: 135px; display: flex; gap: 5px; overflow: hidden; }
  .person { flex: 0 0 136px; height: 135px; background: linear-gradient(160deg, #9c9c9c, #3f3f3f); }
  .person:nth-child(even) { background: linear-gradient(160deg, #c9c9c9, #555); }
  .person.tone { background: linear-gradient(160deg, #b8856a, #3b2a22); }

  /* Testimonial */
  .quote { left: 0; top: 1557px; width: 1200px; height: 153px; background: var(--panel); }
  .quote p { position: absolute; top: 26px; width: 100%; text-align: center; font-family: "Arimo", Arial, sans-serif; font-size: 14.5px; line-height: 24px; color: var(--text-grey); }
  .quote .mark { color: #c8c8c8; font-size: 34px; font-family: Georgia, serif; vertical-align: -10px; }
  .quote .author { position: absolute; top: 86px; width: 100%; text-align: center; font-family: "Arimo", Arial, sans-serif; font-size: 15.5px; color: var(--text-grey); }
  .quote .author b { color: var(--title-blue); font-weight: 400; }
  .notch { left: 582px; top: 1690px; }

  /* Contact */
  .contact-title { top: 1745px; width: 100%; text-align: center; color: var(--title-blue); font-size: 27px; font-weight: 700; }
  .form-intro { left: 131px; top: 1802px; font-size: 13.5px; color: #777; }
  .field { border: 1px solid #d6d6d6; border-radius: 3px; background: var(--white); font-size: 13.5px; color: #888; padding: 10px 13px; }
  .submit { left: 131px; top: 2061px; width: 89px; height: 39px; background: var(--navy); color: var(--white); font-size: 13px; font-weight: 700; text-align: center; line-height: 39px; border-radius: 2px; }
  .touch { left: 864px; top: 1798px; width: 204px; }
  .touch h4 { font-size: 14px; color: var(--title-blue); font-weight: 700; margin-bottom: 12px; }
  .touch-item { display: flex; gap: 16px; padding: 12px 0 12px 4px; border-bottom: 1px solid var(--line); font-size: 12px; line-height: 16.5px; color: #666; }
  .touch-item svg { flex: 0 0 18px; margin-top: 1px; }
  .touch-item .mail { color: var(--title-blue); }

  /* Footer */
  .site-footer { left: 0; top: 2127px; width: 1200px; height: 103px; background: var(--footer-blue); color: var(--white); }
  .footer-nav { position: absolute; top: 28px; width: 100%; text-align: center; font-size: 14px; }
  .footer-nav i { font-style: normal; margin: 0 10px; }
  .footer-links { position: absolute; top: 64px; width: 100%; text-align: center; font-size: 11.5px; }
  .footer-links span { margin: 0 6px; }
  .footer-code { position: absolute; left: 1094px; top: 36px; font-size: 13px; }
</style>
</head>
<body>

<section class="abs hero">
  <div class="hero-visual" role="img" aria-label="Laboratory scientist in gloves holding a test tube of red sample"></div>
  <h1 class="abs hero-title">NEQUE PORRO QUISQUAM</h1>
  <p class="abs hero-sub">NEQUE PORRO QUISQUAM EST<br>QUI DOLOREM IPSUM QUIA</p>
  <a class="abs btn btn-register">REGISTER</a>
  <a class="abs btn btn-login">LOGIN HERE</a>
  <div class="abs slider-nav">
    <svg width="98" height="60" viewBox="0 0 98 60">
      <polyline points="32,20 24,30 32,40" fill="none" stroke="#16498f" stroke-width="4"/>
      <polyline points="66,20 74,30 66,40" fill="none" stroke="#16498f" stroke-width="4"/>
    </svg>
  </div>
</section>

<header class="abs site-header">
  <div class="brand"><span class="brand-dot"></span><span class="brand-name">VONTAREX</span></div>
  <div class="social"><span></span><span></span><span></span><span></span><span></span></div>
  <nav class="main-nav">
    <span class="active">HOME</span><span>SERVICES</span><span>ABOUT US</span><span>CLIENTS</span><span>CONTACT US</span>
  </nav>
</header>

<section class="abs team">
  <h2 class="team-title">ENHANCING YOUR TEAM</h2>
  <div class="team-card" style="left:115px">
    <div class="team-photo photo-lab" role="img" aria-label="Scientist working at a microscope"></div>
    <h3>Neque porro quisquam</h3>
    <p>Lorem ipsum dolor sit amet, consectetur adipisicing<br>sed do eiusmod tempor incididunt ut labore.</p>
  </div>
  <div class="team-card" style="left:448px">
    <div class="team-photo photo-glass" role="img" aria-label="Researcher examining a sample in the lab"></div>
    <h3>Neque porro quisquam</h3>
    <p>Lorem ipsum dolor sit amet, consectetur adipisicing<br>sed do eiusmod tempor incididunt ut labore.</p>
  </div>
  <div class="team-card" style="left:781px">
    <div class="team-photo photo-vial" role="img" aria-label="Gloved hand holding a blood sample tube"></div>
    <h3>Neque porro quisquam</h3>
    <p>Lorem ipsum dolor sit amet, consectetur adipisicing<br>sed do eiusmod tempor incididunt ut labore.</p>
  </div>
</section>

<h2 class="abs welcome-title">WELCOME TO VONTAREX</h2>
<p class="abs welcome-text">At vero eos et accusamus et iusto odio dignissimos ducimus qui blanditiis praesentium voluptatum deleniti atque corrupti quos dolores et quas molestias excepturi sint occaecati cupiditate non provident, similique sunt in culpa qui officia deserunt mollitia animi, id est laborum et dolorum fuga. Et harum quidem rerum facilis est et expedita distinctio. Nam libero temporeAt vero eos et accusamus et iusto odio dignissimos ducimus qui blanditiis praesentiu voluptatum deleniti atque corrupti quos dolores et quas molestias excepturi sint occaeca.lores et quas molestias excepturi sint occaeca.</p>
<a class="abs btn-more">Read More Information</a>

<div class="abs people">
  <div class="person" role="img" aria-label="Team member portrait"></div>
  <div class="person" role="img" aria-label="Team member portrait"></div>
  <div class="person" role="img" aria-label="Team member portrait"></div>
  <div class="person" role="img" aria-label="Team member portrait"></div>
  <div class="person tone" role="img" aria-label="Team member portrait"></div>
  <div class="person" role="img" aria-label="Team member portrait"></div>
  <div class="person" role="img" aria-label="Team member portrait"></div>
  <div class="person" role="img" aria-label="Team member portrait"></div>
  <div class="person" role="img" aria-label="Team member portrait"></div>
</div>

<section class="abs quote">
  <p><span class="mark">&ldquo;</span> Lorem ipsum dolor sit amet, consectetur adipisicing elit, sed do eiusmod tempor incididunt ut labore et dolore magna &nbsp;lorem ipsum gg.<br>Ut enim ad minim veniam, quis nostrud exercitation ullamco laboris nisi ut aliquip ex ea commodo consequat. <span class="mark">&rdquo;</span></p>
  <div class="author"><b>Alan Porter</b> , city name web designer</div>
</section>
<svg class="abs notch" width="36" height="20" viewBox="0 0 36 20"><polygon points="0,20 18,2 36,20" fill="#ffffff"/></svg>

<h2 class="abs contact-title">CONTACT US</h2>
<p class="abs form-intro">Fill your Details and get Job!!</p>
<div class="abs field" style="left:131px;top:1838px;width:330px;height:39px">Your Name:</div>
<div class="abs field" style="left:491px;top:1838px;width:330px;height:39px">Your Phone:</div>
<div class="abs field" style="left:131px;top:1897px;width:330px;height:39px">Your Email:</div>
<div class="abs field" style="left:491px;top:1897px;width:330px;height:39px">Date &amp; Tim:</div>
<div class="abs field" style="left:131px;top:1957px;width:690px;height:84px">Comments:</div>
<a class="abs submit">SUBMIT</a>

<aside class="abs touch">
  <h4>GET IN TOUCH</h4>
  <div class="touch-item">
    <svg width="18" height="18" viewBox="0 0 18 18"><circle cx="9" cy="9" r="7" fill="none" stroke="#aaa" stroke-width="1.6"/><polyline points="9,5 9,9 12,10" fill="none" stroke="#aaa" stroke-width="1.6"/></svg>
    <div>Time 8:50am<br>Time 8:50Pm</div>
  </div>
  <div class="touch-item">
    <svg width="18" height="18" viewBox="0 0 18 18"><path d="M9 17 C4 11 4 9 4 7 a5 5 0 0 1 10 0 c0 2 0 4 -5 10z" fill="#aaa"/><circle cx="9" cy="7" r="2" fill="#fff"/></svg>
    <div>Lorem ipsum dolor sit amet, consectetur adipisicing elit, sed do eiusmod</div>
  </div>
  <div class="touch-item">
    <svg width="18" height="18" viewBox="0 0 18 18"><path d="M4 2 l3 0 l1 4 l-2 1.5 c1 2 2.5 3.5 4.5 4.5 l1.5 -2 l4 1 l0 3 c0 1 -1 2 -2 2 C7 16 2 11 2 4 c0 -1 1 -2 2 -2z" fill="#aaa"/></svg>
    <div>555010234<br>0700555014</div>
  </div>
  <div class="touch-item">
    <svg width="18" height="18" viewBox="0 0 18 18"><rect x="2" y="4" width="14" height="10" fill="none" stroke="#aaa" stroke-width="1.6"/><polyline points="2,4 9,10 16,4" fill="none" stroke="#aaa" stroke-width="1.6"/></svg>
    <div class="mail">Mail@quellbrookmail.com</div>
  </div>
</aside>

<footer class="abs site-footer">
  <nav class="footer-nav">HOME <i>//</i> SERVICES <i>//</i> ABOUT US <i>//</i> CLIENTS <i>//</i> CONTACT US</nav>
  <div class="footer-links"><span>Copyright ©2014 All Rights Reserved</span><span>Privacy Policy</span><span>Terms &amp; Conditions</span><span>Feedback</span><span>Site Map</span><span>Corvalin International</span><span>Members of Brennhart Group</span><span>Contact Us</span></div>
  <div class="footer-code">C4</div>
</footer>

</body>
</html>
```